New banner graphics for Kelbro.com website

I've developed a software tool that helps businesses ensure they are working on their most valuable and important work.

I would like a banner graphic for my home page (www.kelbro.com) that can somehow capture the value of focus and intentional outcomes.

I had an initial thought of a starry sky that shifts focus to a few bright stars, but while that might sound ok, I think my idea is lame hence I'm coming to you guys.

My sites two primary colors are a soft purple and gray.
#919EC1(purple)
#9E9E9E (gray)

Target Market(s)

B2B for enterprises. Typical customers are CFOs, CIOs/Heads of IT

Industry/Entity Type

Business Software

Number of Pages Required

1 page

Font styles to use
Sans Serif

Colors
b8a6cd
cedeed

Requirements
Must have
• I use Divi as my Wordpress theme and the current main landing page can be seen at www.kelbro.com.
• My logo colors are:
• #919EC1(purple)
• #9E9E9E (gray)
Should not have
• Lots of distraction or visual "noise". I want to re-enforce the message that my software is focused on their business and not my products or website.

```html
<!DOCTYPE html>
<html lang="en">
<head>
<meta charset="utf-8">
<title>Kelbro — Our Focus Is You</title>
<link href="https://fonts.googleapis.com/css2?family=Open+Sans:wght@400&family=Raleway:wght@300;400&family=Roboto:wght@100;300&display=swap" rel="stylesheet">
<style>
  :root {
    --page: #ffffff;
    --ink: #1b1b1b;
    --muted: #5a5a5a;
    --accent: #5d6385;
    --brand-purple: #919ec1;
    --brand-gray: #9e9e9e;
    --search: #e0457b;
    --sky-top: #3c3570;
    --sky-mid: #5b4a8a;
    --sky-low: #231d42;
    --ground: #07060c;
  }
  * { margin: 0; padding: 0; box-sizing: border-box; }
  html, body { width: 1200px; height: 1000px; overflow: hidden; background: var(--page); }
  .canvas { position: relative; width: 1200px; height: 1000px; overflow: hidden; }

  .hero {
    position: absolute; left: 4px; top: 0; width: 1094px; height: 580px;
    background: linear-gradient(160deg, var(--sky-top) 0%, var(--sky-mid) 38%, var(--sky-low) 62%, var(--ground) 78%, var(--ground) 100%);
  }
  .hero-tagline {
    position: absolute; left: 86px; top: 80px;
    font-family: "Open Sans", sans-serif; font-weight: 400; font-size: 38px;
    color: #fff; letter-spacing: 0.5px;
    text-shadow: 0 2px 6px rgba(0,0,0,0.6);
  }

  .desktop-heading {
    position: absolute; left: 0; top: 650px; width: 1110px; text-align: center;
    font-family: "Roboto", sans-serif; font-weight: 100; font-size: 88px; line-height: 96px;
    color: var(--ink);
  }
  .desktop-points {
    position: absolute; left: 0; top: 902px; width: 1110px; text-align: center;
    font-family: "Raleway", sans-serif; font-weight: 300; font-size: 44px; line-height: 48px;
    color: var(--muted);
  }
  .highlight { color: var(--accent); }

  .mobile {
    position: absolute; left: 699px; top: 163px; width: 472px; height: 694px;
    background: var(--page);
    box-shadow: 0 10px 40px rgba(0,0,0,0.25), 0 2px 8px rgba(0,0,0,0.15);
  }
  .mobile-header {
    position: relative; height: 58px; border-bottom: 2px solid #444;
  }
  .mobile-brand {
    position: absolute; left: 34px; top: 13px;
    font-family: "Raleway", sans-serif; font-weight: 400; font-size: 24px;
    color: var(--brand-purple); letter-spacing: 0.5px;
  }
  .mobile-search { position: absolute; left: 384px; top: 22px; }
  .mobile-menu { position: absolute; left: 424px; top: 23px; }
  .mobile-hero {
    position: absolute; left: 8px; top: 61px; width: 456px; height: 239px;
    background: linear-gradient(160deg, var(--sky-top) 0%, var(--sky-mid) 38%, var(--sky-low) 62%, var(--ground) 80%, var(--ground) 100%);
  }
  .mobile-tagline {
    position: absolute; left: 35px; top: 33px;
    font-family: "Open Sans", sans-serif; font-size: 15px; color: #fff;
    text-shadow: 0 1px 3px rgba(0,0,0,0.6);
  }
  .mobile-heading {
    position: absolute; left: 0; top: 331px; width: 472px; text-align: center;
    font-family: "Roboto", sans-serif; font-weight: 300; font-size: 37px; line-height: 39px;
    color: var(--ink);
  }
  .mobile-points {
    position: absolute; left: 20px; top: 436px; width: 432px; text-align: center;
    list-style: none;
    font-family: "Raleway", sans-serif; font-weight: 400; font-size: 18px; line-height: 20px;
    color: var(--muted);
  }
  .mobile-points li { margin-bottom: 18px; }
</style>
</head>
<body>
<main class="canvas">
  <section class="hero" role="img" aria-label="Night sky full of stars over a dark ridge, a lone figure sitting on a rock">
    <p class="hero-tagline">OUR FOCUS IS YOU.</p>
  </section>

  <h1 class="desktop-heading">Is Your Business<br>Strategy</h1>
  <p class="desktop-points"><span class="highlight">WRITTEN DOWN</span> or LOOSE THOUGHTS –<br>ON THE BEST OF DAYS.</p>

  <section class="mobile">
    <header class="mobile-header">
      <span class="mobile-brand">kelbro</span>
      <svg class="mobile-search" width="14" height="14" viewBox="0 0 14 14" aria-label="Search">
        <circle cx="8" cy="6" r="4.5" fill="none" stroke="var(--search)" stroke-width="1.5"/>
        <line x1="4.8" y1="9.2" x2="1" y2="13" stroke="var(--search)" stroke-width="1.5"/>
      </svg>
      <svg class="mobile-menu" width="14" height="12" viewBox="0 0 14 12" aria-label="Menu">
        <rect y="0" width="14" height="2" fill="#444"/>
        <rect y="5" width="14" height="2" fill="#444"/>
        <rect y="10" width="14" height="2" fill="#444"/>
      </svg>
    </header>
    <div class="mobile-hero" role="img" aria-label="Night sky full of stars over a dark ridge, a lone figure sitting on a rock">
      <p class="mobile-tagline">OUR FOCUS IS YOU.</p>
    </div>
    <h2 class="mobile-heading">Is Your Business<br>Strategy</h2>
    <ul class="mobile-points">
      <li><span class="highlight">WRITTEN DOWN</span> or LOOSE THOUGHTS –<br>ON THE BEST OF DAYS.</li>
      <li><span class="highlight">DRIVING PROJECTS</span> or JUST A SET OF<br>SLIDES TACKED TO WALLS</li>
      <li><span class="highlight">SHARED WITH THE TEAM</span> or KEPT TOP<br>SECRET JUST TO BE SAFE</li>
      <li><span class="highlight">MEASURABLE</span> or MORE ART THAN SCIENCE</li>
    </ul>
  </section>
</main>
</body>
</html>
```